Business cards and letterhead
UK size business cards/letterhead
Project: Business cards and letterhead
Business cards and letterhead - Information Technology
Creative Brief
Professional
Gareth Pellow
Director
148 Ashcombe Lane Twickenham Middlesex TW4 3QR
gareth.pellow@corvalisen.com
www.corvalisen.com
Note business card needs to be UK-sized (i.e. 85 x 55)/double sided, and the letterhead suitable for A4 paper Back of card can contain some/all of suggested text, depending upon how well it fits
ECM Consultancy Services - Project Management and Delivery - Implementation Planning - Data Conversion Management - Existing System Reviews - Software Design and Development - Test Strategy Definition and Execution

```html
<!DOCTYPE html>
<html lang="en">
<head>
<meta charset="utf-8">
<title>Corvalisen Business Cards</title>
<link href="https://fonts.googleapis.com/css2?family=Open+Sans:wght@400;600;700;800&family=Cinzel:wght@400&display=swap" rel="stylesheet">
<style>
  :root {
    --backdrop: #d9c3a1;
    --paper: #ffffff;
    --charcoal: #26272a;
    --charcoal-deep: #141416;
    --blue: #1a9fd6;
    --blue-deep: #0b5f8c;
    --blue-light: #3fbfef;
    --grey: #9a9ea3;
    --grey-light: #d4d6d9;
    --ink: #3a3c40;
    --ink-soft: #6b6e73;
    --label: #3b3027;
  }
  * { box-sizing: border-box; margin: 0; padding: 0; }
  html, body { width: 1200px; height: 794px; overflow: hidden; }
  body {
    background: var(--backdrop);
    font-family: "Open Sans", Arial, sans-serif;
    position: relative;
  }
  .card {
    position: absolute;
    width: 542px;
    height: 252px;
    border-radius: 14px;
    overflow: hidden;
    box-shadow: 0 3px 8px rgba(0,0,0,.28);
  }
  .front-a { left: 30px; top: 43px; background: var(--paper); }
  .front-b { left: 636px; top: 43px; background: linear-gradient(160deg, #3a3b3f 0%, var(--charcoal) 45%, var(--charcoal-deep) 100%); }
  .back-a { left: 30px; top: 410px; background: radial-gradient(ellipse at 70% 35%, var(--blue-light) 0%, var(--blue) 35%, var(--blue-deep) 100%); }
  .back-b { left: 636px; top: 410px; background: radial-gradient(ellipse at 70% 35%, #4a4b50 0%, #2c2d31 45%, var(--charcoal-deep) 100%); }

  .swoosh { position: absolute; left: 0; bottom: 0; width: 542px; height: 252px; }

  .brand {
    position: absolute;
    left: 34px;
    top: 128px;
    display: flex;
    align-items: center;
    gap: 10px;
    font-weight: 800;
    font-size: 33px;
    letter-spacing: 1px;
    color: var(--charcoal);
  }
  .brand-dot { width: 18px; height: 18px; border-radius: 50%; background: var(--blue); }
  .front-b .brand { color: #e6e7e9; }

  .contact { position: absolute; left: 300px; top: 40px; }
  .contact-name { font-size: 15px; font-weight: 600; color: var(--blue); line-height: 1.2; }
  .contact-role { font-size: 11px; color: var(--ink-soft); margin-bottom: 14px; }
  .front-b .contact-role { color: #b9bbbf; }
  .contact-list { list-style: none; }
  .contact-list li {
    display: flex; align-items: flex-start; gap: 7px;
    font-size: 10.5px; line-height: 1.35; color: var(--ink); margin-bottom: 5px;
  }
  .front-b .contact-list li { color: #d3d5d8; }
  .contact-list svg { flex: none; width: 11px; height: 11px; margin-top: 2px; }

  .services { position: absolute; left: 24px; top: 100px; }
  .services-title { font-size: 17px; font-weight: 600; color: #fff; margin-bottom: 8px; }
  .back-b .services-title { color: var(--blue-light); }
  .services-list { list-style: none; }
  .services-list li {
    display: flex; align-items: center; gap: 8px;
    font-size: 11.5px; line-height: 18px; color: #fff;
  }
  .back-b .services-list li { color: #e3e4e6; }
  .services-list li::before {
    content: ""; width: 7px; height: 7px; border-radius: 50%; background: #fff; flex: none;
  }
  .back-b .services-list li::before { background: var(--blue-light); }

  .glow { position: absolute; right: 70px; top: 20px; width: 200px; height: 200px; border-radius: 50%;
    background: radial-gradient(circle, rgba(255,255,255,.12) 0%, rgba(255,255,255,0) 70%); }

  .caption {
    position: absolute; width: 542px; text-align: center;
    font-family: "Cinzel", Georgia, serif; font-size: 22px; letter-spacing: 3px;
    color: var(--label);
  }
  .caption-front-a { left: 30px; top: 342px; }
  .caption-front-b { left: 636px; top: 342px; }
  .caption-back-a { left: 30px; top: 726px; }
  .caption-back-b { left: 636px; top: 726px; }
</style>
</head>
<body>

<svg width="0" height="0" style="position:absolute">
  <defs>
    <linearGradient id="band-blue" x1="0" y1="0" x2="1" y2="0">
      <stop offset="0" stop-color="#0b5f8c"/>
      <stop offset=".5" stop-color="#1a9fd6"/>
      <stop offset="1" stop-color="#0d6fa3"/>
    </linearGradient>
    <linearGradient id="band-grey" x1="0" y1="0" x2="1" y2="0">
      <stop offset="0" stop-color="#cfd1d4"/>
      <stop offset=".5" stop-color="#8f9398"/>
      <stop offset="1" stop-color="#c9cbce"/>
    </linearGradient>
  </defs>
</svg>

<!-- Front A -->
<section class="card front-a">
  <svg class="swoosh" viewBox="0 0 542 252" aria-hidden="true">
    <path d="M0 200 Q260 160 542 178 L542 252 L0 252Z" fill="url(#band-grey)"/>
    <path d="M0 214 Q280 178 542 196 L542 252 L0 252Z" fill="url(#band-blue)"/>
    <path d="M0 238 Q300 208 542 226 L542 252 L0 252Z" fill="#ffffff" opacity=".9"/>
  </svg>
  <div class="brand"><span class="brand-dot"></span>CORVALISEN</div>
  <div class="contact">
    <p class="contact-name">Gareth Pellow</p>
    <p class="contact-role">Director</p>
    <ul class="contact-list">
      <li><svg viewBox="0 0 12 12"><path d="M6 1 L11 6 H9.5 V11 H2.5 V6 H1Z" fill="#6b6e73"/></svg><span>148 Ashcombe Lane Twickenham<br>Middlesex TW4 3QR</span></li>
      <li><svg viewBox="0 0 12 12"><path d="M3 1 L5 3.5 L4 5 Q5 7 7 8 L8.5 7 L11 9 L9.5 11 Q4 10.5 1 3Z" fill="#6b6e73"/></svg><span>+44-7700-900-418</span></li>
      <li><svg viewBox="0 0 12 12"><circle cx="6" cy="6" r="5" fill="#1a9fd6"/><text x="6" y="8.5" font-size="7" text-anchor="middle" fill="#fff" font-family="Arial">@</text></svg><span>gareth.pellow@corvalisen.com</span></li>
      <li><svg viewBox="0 0 12 12"><circle cx="6" cy="6" r="5" fill="none" stroke="#6b6e73" stroke-width="1.2"/><path d="M1 6 H11 M6 1 Q3 6 6 11 M6 1 Q9 6 6 11" fill="none" stroke="#6b6e73" stroke-width=".9"/></svg><span>www.corvalisen.com</span></li>
    </ul>
  </div>
</section>

<!-- Front B -->
<section class="card front-b">
  <svg class="swoosh" viewBox="0 0 542 252" aria-hidden="true">
    <path d="M0 200 Q260 160 542 178 L542 252 L0 252Z" fill="url(#band-grey)"/>
    <path d="M0 214 Q280 178 542 196 L542 252 L0 252Z" fill="url(#band-blue)"/>
    <path d="M0 238 Q300 208 542 226 L542 252 L0 252Z" fill="#1d1e21"/>
  </svg>
  <div class="brand"><span class="brand-dot"></span>CORVALISEN</div>
  <div class="contact">
    <p class="contact-name">Gareth Pellow</p>
    <p class="contact-role">Director</p>
    <ul class="contact-list">
      <li><svg viewBox="0 0 12 12"><path d="M6 1 L11 6 H9.5 V11 H2.5 V6 H1Z" fill="#b9bbbf"/></svg><span>148 Ashcombe Lane Twickenham<br>Middlesex TW4 3QR</span></li>
      <li><svg viewBox="0 0 12 12"><path d="M3 1 L5 3.5 L4 5 Q5 7 7 8 L8.5 7 L11 9 L9.5 11 Q4 10.5 1 3Z" fill="#b9bbbf"/></svg><span>+44-7700-900-418</span></li>
      <li><svg viewBox="0 0 12 12"><circle cx="6" cy="6" r="5" fill="#1a9fd6"/><text x="6" y="8.5" font-size="7" text-anchor="middle" fill="#fff" font-family="Arial">@</text></svg><span>gareth.pellow@corvalisen.com</span></li>
      <li><svg viewBox="0 0 12 12"><circle cx="6" cy="6" r="5" fill="none" stroke="#b9bbbf" stroke-width="1.2"/><path d="M1 6 H11 M6 1 Q3 6 6 11 M6 1 Q9 6 6 11" fill="none" stroke="#b9bbbf" stroke-width=".9"/></svg><span>www.corvalisen.com</span></li>
    </ul>
  </div>
</section>

<p class="caption caption-front-a">Business Card Front A</p>
<p class="caption caption-front-b">Business Card Front B</p>

<!-- Back A -->
<section class="card back-a">
  <div class="glow"></div>
  <div class="services">
    <h2 class="services-title">ECM Consultancy Services</h2>
    <ul class="services-list">
      <li>Project Management and Delivery</li>
      <li>Implementation Planning</li>
      <li>Data Conversion Management</li>
      <li>Existing System Reviews</li>
      <li>Software Design and Development</li>
      <li>Test Strategy Definition and Execution</li>
    </ul>
  </div>
</section>

<!-- Back B -->
<section class="card back-b">
  <div class="glow"></div>
  <div class="services">
    <h2 class="services-title">ECM Consultancy Services</h2>
    <ul class="services-list">
      <li>Project Management and Delivery</li>
      <li>Implementation Planning</li>
      <li>Data Conversion Management</li>
      <li>Existing System Reviews</li>
      <li>Software Design and Development</li>
      <li>Test Strategy Definition and Execution</li>
    </ul>
  </div>
</section>

<p class="caption caption-back-a">Business Card Back A</p>
<p class="caption caption-back-b">Business Card Back B</p>

</body>
</html>
```